Zielgruppe
brinko handel ist eine Vertriebsagentur, die sich ausschließlich auf den BtoB Vertrieb spezialisiert hat. Wir agieren seit 19 Jahren am Markt und sind mehrfach ausgezeichneter Exzellenzberater des Mittelstandes. Wir unterstützen mittelständische Unternehmen, Familienunternehmen, Start up´s in der Wachstumsphase und Großkonzerne in der Industrie und im Dienstleistungsbereich. Ansprechpartner für uns sind Vertriebsleiter und GF´s in den Unternehmen.
Aufgabenstellung
Wir möchten unsere Angebotsvorlage neu im Layout neu designen lassen. Sie soll unsere Arbeitsweise zielgenau - authentisch - pfiffig widerspiegeln. Ich möchte gerne eine moderne und klare Struktur. Auf einer Seite sollen unsere USP´s dargestellt werden und auf ein - zwei Seiten ist das Angebot - in den folgenden Seiten sind die Vertragsinhalte.

```html
<!DOCTYPE html>
<html lang="de">
<head>
<meta charset="utf-8">
<title>Angebotsvorlage brinko handel</title>
<link rel="stylesheet" href="https://fonts.googleapis.com/css2?family=Arimo:wght@400;700&display=swap">
<style>
:root{
  --backdrop:#e6e6e6;
  --paper:#ffffff;
  --ink:#3a3a3a;
  --blue:#1f4a8c;
  --coral:#ec7461;
  --rule:#d6d6d6;
}
*{box-sizing:border-box;margin:0;padding:0}
html,body{width:1200px;height:1200px;overflow:hidden;background:var(--backdrop)}
body{font-family:"Arimo",Arial,sans-serif;color:var(--ink);position:relative}
.page{position:absolute;top:215px;width:540px;height:770px;background:var(--paper);
  box-shadow:0 6px 18px rgba(0,0,0,.12);padding:0 36px}
.page--confirm{left:45px}
.page--offer{left:615px}
.page-header{position:relative;height:58px;border-bottom:3px solid var(--rule)}
.page-number{position:absolute;left:0;top:38px;font-size:8px}
.offer-number{position:absolute;right:0;top:34px;font-size:9px;font-weight:700;color:var(--coral)}
.page--confirm .offer-number{left:0;right:auto}
.page-title{color:var(--blue);font-size:25px;font-weight:700;margin:42px 0 30px}
.section-title{color:var(--blue);font-size:16.5px;font-weight:400;margin:18px 0 6px}
.body-text{font-size:9.2px;line-height:1.32}
.subsection{color:var(--blue);font-size:9.2px;margin-top:10px}
.note{font-size:9.2px;line-height:1.32;margin-top:22px}
.page-footer{position:absolute;left:36px;right:36px;bottom:16px;border-top:3px solid var(--rule);
  padding-top:10px;font-size:8px;white-space:nowrap}
.accent{position:absolute;left:0;top:545px}
.party{font-size:10px;line-height:1.25;margin-top:34px}
.consent{font-size:10px;line-height:1.35;margin-top:34px}
.variants{margin-top:72px;font-size:10px}
.variant{display:flex;align-items:center;gap:26px;margin-bottom:12px}
.checkbox{width:15px;height:15px;border:1.3px solid #555;margin-left:18px}
.signature{margin-top:78px;font-size:10px}
.signature-row{margin-bottom:24px}
</style>
</head>
<body>

<section class="page page--confirm">
  <header class="page-header"><span class="offer-number">Angebot-Nr. 20221008</span></header>
  <h1 class="page-title">ANGEBOTSBESTÄTIGUNG</h1>
  <p class="party">Auftraggeber<br>Norvand Logistik SE &amp; Co. KG</p>
  <p class="party" style="margin-top:56px">Auftragnehmer<br>brinko handel GmbH<br>Lindenweg 7<br>91000 Musterstadt</p>
  <p class="consent">Hiermit bestätige ich als Auftraggeber das Angebot Nr. 20221008<br>und erteile entsprechend dem Angebot den Auftrag.</p>
  <div class="variants">
    <div class="variant"><span class="checkbox"></span><span>Variante a &nbsp;&nbsp;- 15h Vertriebsunterstützung / Woche</span></div>
    <div class="variant"><span class="checkbox"></span><span>Variante b &nbsp;&nbsp;- 20h Vertriebsunterstützung / Woche</span></div>
  </div>
  <div class="signature">
    <p class="signature-row">Ort, Datum: ______________________________________</p>
    <p class="signature-row">Name / Vorname in Druckbuchstaben: ____________________</p>
    <p class="signature-row">Unterschrift: ______________________________________</p>
    <p class="signature-row">Firmenstempel</p>
  </div>
  <footer class="page-footer">Marlen Voss-Hardt &nbsp;|&nbsp; +49 (0) 170 000 123 4 &nbsp;|&nbsp; mvh@brinko-handel.de &nbsp;|&nbsp; Lindenweg 7 &nbsp;|&nbsp; 91000 Musterstadt</footer>
</section>

<section class="page page--offer">
  <svg class="accent" width="36" height="190" viewBox="0 0 36 190" aria-hidden="true">
    <path d="M0 0H36V150Q36 178 0 190Z" fill="var(--coral)"/>
  </svg>
  <header class="page-header"><span class="page-number">4</span><span class="offer-number">Angebot-Nr. 20221008</span></header>
  <h1 class="page-title">NEUE KUNDEN AKQUIRIEREN</h1>

  <h2 class="section-title">SETUP-Installation einmalig</h2>
  <p class="body-text">2 h Workshop – Einweisung Mitarbeiterin 2h (1)<br>Abstimmung Prozesse und Schnittstellen<br>Erarbeitung + Coaching Gesprächskonzept / Einwandargumentation</p>

  <h2 class="section-title">TECHNIK-Programmierung einmalig</h2>
  <p class="body-text">Integration firmeninterner Telefonnummer</p>

  <h2 class="section-title">PROJEKTARBEIT</h2>
  <p class="body-text">agieren unter Norvand Logistik SE &amp; Co. KG<br>
  akquirieren auf Entscheiderebene in den Unternehmen Einkauf, Qualitätsmanager, Produktionsleiter<br>
  stellen das Unternehmen mit seinen Dienstleistungen und Vorteilen vor und erfragen<br>
  - &nbsp;aktuellen Bedarf an Logistik<br>
  - &nbsp;wiederkehrende und herausfordernde Destinationen inkl. Tonnagen<br>
  - &nbsp;Zufriedenheit mit dem aktuellen Partner<br>
  eruieren die aktuelle IST-Situation und erfragen ggf. bestehende Partnerschaften / Verträge<br>
  wecken Interesse an den Dienstleistungen und bauen ein vertrauensvolles<br>
  Verhältnis auf<br>
  - &nbsp;erarbeiten bedarfsorientierte Wiedervorlagen,<br>
  - &nbsp;koordinieren und bestätigen Termine vor Ort,<br>
  - &nbsp;bleiben am vertriebsorientiert dran Kontakt,<br>
  - &nbsp;erfragen Alternativangebote<br>
  telefonieren aktiv Angeboten nach und erfragen die Entscheidergründe</p>

  <p class="subsection">Adressrecherche &nbsp;/ Adressdaten inkl. Kontaktdaten</p>
  <p class="body-text">Adressselektion nach Unternehmen, Branchen und Regionen</p>

  <p class="subsection">a ) TESTPROJEKT &nbsp;- 15h / Woche – 10 Wochen</p>
  <p class="body-text">14h Akquise/ Recherche + 2h interne Projektabstimmung je Woche<br>garantiert 140 Gespräche / Woche</p>

  <p class="subsection">b ) TESTPROJEKT &nbsp;- 20h / Woche – 10 Wochen</p>
  <p class="body-text">18,5h Akquise/ Recherche + 1,5h interne Projektabstimmung je Woche<br>garantiert 185 Gespräche / Woche</p>

  <p class="note">(1) zzgl. An- und Abfahrt je 85 ct / km<br>&nbsp;&nbsp;&nbsp;&nbsp;&nbsp;zzgl. je Mitarbeiter Aufwandspauschale 250,00 €</p>

  <footer class="page-footer">Marlen Voss-Hardt &nbsp;|&nbsp; +49 (0) 170 000 123 4 &nbsp;|&nbsp; mvh@brinko-handel.de &nbsp;|&nbsp; Lindenweg 7 &nbsp;|&nbsp; 91000 Musterstadt &nbsp;|&nbsp; 09100 555 100 0</footer>
</section>

</body>
</html>
```